hfdhddfgfhfghfghgfhfhfhgfhfhfh

Industry/Entity Type

Painting

Logo Text

KOLBEC Painting

Logo styles of interest
Wordmark Logo
Requirements
Should not have
• Paintbrushes or rollers etc....

```html
<!DOCTYPE html>
<html lang="en">
<head>
<meta charset="utf-8">
<title>KOLBEC Painting – Business Cards</title>
<link rel="stylesheet" href="https://fonts.googleapis.com/css2?family=Montserrat:wght@600;700&family=Open+Sans:wght@400;600&display=swap">
<style>
  :root {
    --backdrop: #e4e6e8;
    --card-white: #ffffff;
    --card-grey: #eef0f2;
    --brand-blue: #1b87cc;
    --brand-blue-dark: #0f6fae;
    --ink: #474c52;
    --ink-soft: #5c6168;
  }
  * { box-sizing: border-box; margin: 0; padding: 0; }
  html, body { width: 1200px; height: 901px; overflow: hidden; }
  body {
    background: var(--backdrop);
    font-family: "Open Sans", Arial, sans-serif;
    display: flex;
    flex-direction: column;
    align-items: center;
    justify-content: center;
    gap: 36px;
  }
  .card {
    position: relative;
    width: 700px;
    height: 400px;
    background: linear-gradient(180deg, var(--card-white), var(--card-grey));
    box-shadow: 0 6px 20px rgba(0,0,0,.18);
    overflow: hidden;
  }
  .card-shapes { position: absolute; inset: 0; width: 100%; height: 100%; }
  .wordmark {
    position: absolute;
    font-family: "Montserrat", Arial, sans-serif;
    font-weight: 700;
    color: var(--ink);
    font-size: 50px;
    line-height: 0.95;
    letter-spacing: 2px;
    text-transform: uppercase;
  }
  .back .wordmark { left: 48px; top: 152px; }
  .front .wordmark { left: 52px; top: 58px; }
  .tagline {
    position: absolute;
    right: 40px;
    top: 252px;
    color: var(--card-white);
    font-size: 19px;
    font-weight: 600;
    letter-spacing: .5px;
  }
  .contact {
    position: absolute;
    left: 68px;
    top: 236px;
    color: var(--ink);
  }
  .contact-name {
    color: var(--brand-blue);
    font-family: "Montserrat", Arial, sans-serif;
    font-weight: 700;
    font-size: 24px;
    letter-spacing: .5px;
  }
  .contact-role { font-size: 17px; margin-bottom: 16px; }
  .contact-row { display: flex; gap: 18px; font-size: 20px; line-height: 1.35; }
  .contact-label { width: 64px; color: var(--brand-blue); font-weight: 600; }
  .abn {
    position: absolute;
    right: 44px;
    top: 222px;
    font-size: 13px;
    color: var(--ink-soft);
    letter-spacing: .5px;
  }
</style>
</head>
<body>

  <section class="card back" aria-label="Card back">
    <svg class="card-shapes" viewBox="0 0 700 400" preserveAspectRatio="none" aria-hidden="true">
      <defs>
        <linearGradient id="blueBack" x1="0" y1="0" x2="1" y2="1">
          <stop offset="0" stop-color="#2596d8"/>
          <stop offset="1" stop-color="#0f6fae"/>
        </linearGradient>
      </defs>
      <path d="M0,292 C240,292 450,250 700,140 V400 H0 Z" fill="url(#blueBack)"/>
      <path d="M330,262 C470,238 590,190 700,118 V126 C590,198 480,244 330,262 Z" fill="var(--brand-blue)"/>
    </svg>
    <div class="wordmark">Kolbec<br>Painting</div>
    <p class="tagline">Residential &amp; Commercial</p>
  </section>

  <section class="card front" aria-label="Card front">
    <svg class="card-shapes" viewBox="0 0 700 400" preserveAspectRatio="none" aria-hidden="true">
      <defs>
        <linearGradient id="blueFront" x1="0" y1="0" x2="1" y2="1">
          <stop offset="0" stop-color="#1f8fd2"/>
          <stop offset="1" stop-color="#147bbf"/>
        </linearGradient>
      </defs>
      <path d="M0,0 H700 V112 C540,132 400,180 0,196 Z" fill="url(#blueFront)"/>
      <path d="M330,196 C470,176 600,146 700,132 V140 C600,156 480,184 330,196 Z" fill="var(--brand-blue)"/>
    </svg>
    <div class="wordmark">Kolbec<br>Painting</div>
    <div class="contact">
      <p class="contact-name">MARTIN KOLBEC</p>
      <p class="contact-role">Managing Director</p>
      <p class="contact-row"><span class="contact-label">Mobile</span><span>0400 555 318</span></p>
      <p class="contact-row"><span class="contact-label">Email</span><span>kolbecpainting@mail.com</span></p>
    </div>
    <p class="abn">ABN 11 230 457 902</p>
  </section>

</body>
</html>
```